Redesign my business cards

I would like pretty much all the same information as my current business cards but redesigned to stand out more and be more unique photo uploaded to show my current business cards don’t mind if you want to remove or replace I for on the back

```html
<!DOCTYPE html>
<html lang="en">
<head>
<meta charset="utf-8">
<title>Varnley Detailing – Business Card</title>
<link rel="stylesheet" href="https://fonts.googleapis.com/css2?family=Exo+2:wght@600;700&family=Poppins:wght@400;500&display=swap">
<style>
  :root {
    --backdrop: #1d1d1f;
    --navy: #13283a;
    --paper: #ffffff;
    --violet: #5a24b8;
    --violet-deep: #4a22b0;
    --plum: #8b3ca6;
    --ink: #1c1c22;
    --rule: #45566a;
    --logo-tint: #7c4fe0;
  }
  * { box-sizing: border-box; margin: 0; padding: 0; }
  html, body { width: 1200px; height: 1108px; overflow: hidden; }
  body {
    background: var(--backdrop);
    font-family: "Poppins", sans-serif;
    color: var(--ink);
    display: flex;
    align-items: center;
    justify-content: center;
    gap: 60px;
  }
  .card {
    position: relative;
    width: 420px;
    height: 680px;
    background: var(--paper);
    border-radius: 26px;
    overflow: hidden;
  }

  /* Front */
  .card-front .top-band {
    position: absolute;
    inset: 0 0 auto 0;
    height: 230px;
    background: var(--navy);
  }
  .card-front .brand-disc {
    position: absolute;
    left: 60px;
    top: 80px;
    width: 300px;
    height: 300px;
    border-radius: 50%;
    background: var(--navy);
    display: flex;
    align-items: center;
    justify-content: center;
    text-align: center;
  }
  .brand-name {
    font-family: "Exo 2", sans-serif;
    font-weight: 600;
    font-size: 24px;
    line-height: 1.3;
    letter-spacing: 5px;
    color: var(--logo-tint);
  }
  .owner {
    position: absolute;
    top: 425px;
    left: 0;
    right: 0;
    text-align: center;
  }
  .owner-name {
    font-family: "Exo 2", sans-serif;
    font-weight: 700;
    font-size: 34px;
    color: var(--violet);
    line-height: 1.1;
  }
  .owner-role {
    font-size: 22px;
    font-weight: 400;
    color: var(--ink);
    margin-top: 2px;
  }
  .divider {
    width: 140px;
    height: 1px;
    background: var(--rule);
    margin: 22px auto 18px;
  }
  .contact-line { font-size: 22px; line-height: 1.35; }
  .contact-line.email { font-size: 20px; }

  /* Back */
  .card-back {
    padding: 34px 32px;
    display: flex;
    flex-direction: column;
    justify-content: center;
    gap: 18px;
  }
  .package { text-align: center; }
  .price-row {
    display: flex;
    align-items: center;
    gap: 6px;
  }
  .price-row::before, .price-row::after {
    content: "";
    flex: 1;
    border-top: 2px dotted var(--ink);
  }
  .price-badge {
    width: 76px;
    height: 76px;
    border-radius: 50%;
    background: linear-gradient(160deg, var(--violet-deep), var(--plum));
    color: var(--paper);
    font-weight: 500;
    font-size: 22px;
    display: flex;
    align-items: center;
    justify-content: center;
  }
  .package-title {
    color: var(--violet);
    font-weight: 500;
    font-size: 17px;
    line-height: 1.4;
    text-transform: uppercase;
    margin: 2px 0 1px;
  }
  .package-desc {
    font-size: 14.5px;
    line-height: 1.3;
    padding: 0 2px;
  }
</style>
</head>
<body>

  <section class="card card-front" aria-label="Card front">
    <div class="top-band"></div>
    <div class="brand-disc">
      <p class="brand-name">VARNLEY<br>DETAILING</p>
    </div>
    <div class="owner">
      <h1 class="owner-name">MILES HARNETT</h1>
      <p class="owner-role">Owner/Operator</p>
      <div class="divider"></div>
      <p class="contact-line">0427516093</p>
      <p class="contact-line email">varnleydetailing@mailbox.com</p>
    </div>
  </section>

  <section class="card card-back" aria-label="Card back – service packages">
    <article class="package">
      <div class="price-row"><span class="price-badge">$150</span></div>
      <h2 class="package-title">Interior Detail</h2>
      <p class="package-desc">Vacume &amp; deep clean of carpets &amp; upholstery or leather treatment interior trim clean &amp; conditions, window polish and treatment, steam clean and stain removal</p>
    </article>
    <article class="package">
      <div class="price-row"><span class="price-badge">$250</span></div>
      <h2 class="package-title">Exterior Detail</h2>
      <p class="package-desc">Extreme wash &amp; polish, exterior trim reviver &amp; protector window polish &amp; treatment, tyre dressing, engine bay cleaned</p>
    </article>
    <article class="package">
      <div class="price-row"><span class="price-badge">$350</span></div>
      <h2 class="package-title">Full Extreme Detail</h2>
      <p class="package-desc">Extreme wash &amp; polish, tyre dressing, engine bay cleaned, vacume &amp; deep clean of carpets &amp; upholstery or leather treatment, interior &amp; exterior trim reviver &amp; protector, window polish and treatment</p>
    </article>
  </section>

</body>
</html>
```